Larkfield Clinic Marketing Flyer

We are a new medical practice in the community and need a flyer to send to other medical offices to inform of our services. We just completed our logo with PixelGuild and would like to incorporate that plus our marketing content into the flyer. Our medical practice has 2 divisions: (1)Mental Health/Psychiatry and (2) Migraine and Neurospasticity Management. Please see website for content and provider photos at www.LarkfieldCare.example

Target Market(s)

Other Healthcare Professionals in the Community

Industry/Entity Type

Medical

Requirements
Must have
• Photos of all 5 healthcare providers, phone number, address, logo

```html
<!DOCTYPE html>
<html lang="en">
<head>
<meta charset="utf-8">
<title>Larkfield Clinic – Provider Flyer</title>
<link href="https://fonts.googleapis.com/css2?family=DM+Serif+Display&family=Roboto:wght@400;500;700&display=swap" rel="stylesheet">
<style>
  :root {
    --bg: #eef9d9;
    --paper: #ffffff;
    --forest: #0f4a25;
    --forest-deep: #0b3a1c;
    --lime: #b5df78;
    --mint: #dff2c4;
    --ink: #1d2a22;
    --teal: #1f9a8a;
  }
  * { box-sizing: border-box; margin: 0; padding: 0; }
  html, body { width: 1200px; height: 1200px; overflow: hidden; }
  body { background: var(--bg); font-family: "Roboto", Arial, sans-serif; color: var(--ink); position: relative; }

  .flyer { position: absolute; left: 180px; top: 56px; width: 840px; height: 1088px; background: var(--paper); overflow: hidden; box-shadow: 0 10px 30px rgba(40,80,20,.18); }
  .abs { position: absolute; }

  /* header */
  .brand { left: 34px; top: 80px; width: 230px; display: flex; align-items: center; gap: 10px; }
  .brand-dot { width: 34px; height: 34px; border-radius: 50%; background: var(--teal); flex: none; }
  .brand-name { font-family: "DM Serif Display", Georgia, serif; font-size: 28px; line-height: 1.05; color: var(--teal); }
  .hero-shape { left: 270px; top: -40px; width: 420px; height: 260px; background: var(--mint); border-radius: 0 0 0 220px; }
  .hero-photo { left: 610px; top: 0; width: 230px; height: 206px; background: linear-gradient(135deg, #e9e6df 0%, #c9c3b6 45%, #d6a62a 70%, #8e8a80 100%); }
  .headline { left: 296px; top: 46px; font-family: "DM Serif Display", Georgia, serif; font-weight: 400; font-size: 42px; line-height: 1.05; color: var(--forest-deep); }

  /* section bands */
  .band { left: 0; width: 840px; height: 40px; background: var(--lime); display: flex; align-items: center; justify-content: center; }
  .band h2 { font-family: "DM Serif Display", Georgia, serif; font-weight: 400; font-size: 27px; color: var(--forest-deep); }
  .intro { left: 50px; width: 740px; font-size: 13.5px; line-height: 1.4; text-align: center; }

  /* providers */
  .provider-panel { left: 0; top: 336px; width: 840px; height: 364px; background: var(--forest); }
  .provider-curve { left: -60px; top: 400px; width: 290px; height: 290px; border-radius: 50%; background: var(--forest-deep); }
  .providers { left: 24px; top: 350px; width: 792px; display: flex; justify-content: space-between; }
  .provider { width: 186px; text-align: center; color: #fff; }
  .provider-photo { width: 130px; height: 130px; margin: 0 auto 8px; background: radial-gradient(circle at 50% 40%, #b9a291 0 26%, #6f7f82 27%, #3f4a4d 100%); }
  .provider-name { font-size: 14px; line-height: 1.25; margin-bottom: 6px; }
  .provider-bio { font-size: 10.5px; line-height: 1.32; }

  /* migraine */
  .spec-circle { left: 200px; top: 798px; width: 100px; height: 100px; border-radius: 50%; background: var(--mint); }
  .specialist { left: 0; top: 815px; width: 260px; height: 223px; background: var(--forest-deep); color: #fff; text-align: center; padding: 10px 16px 0; }
  .specialist-photo { width: 150px; height: 100px; margin: 0 auto 8px; background: linear-gradient(160deg, #7a5a3a 0%, #b8977a 45%, #e7dcc8 100%); }
  .specialist-bio { font-size: 10.5px; line-height: 1.3; }
  .steps { left: 260px; top: 815px; width: 580px; height: 223px; display: flex; }
  .step { flex: 1; text-align: center; padding: 24px 16px 0; }
  .step.alt { background: var(--mint); }
  .step svg { width: 48px; height: 48px; margin-bottom: 8px; }
  .step h3 { font-family: "DM Serif Display", Georgia, serif; font-weight: 400; font-size: 20px; line-height: 1.1; color: var(--forest-deep); margin-bottom: 10px; }
  .step p { font-size: 11px; line-height: 1.35; }

  /* footer */
  .footer { left: 0; top: 1038px; width: 840px; height: 50px; background: var(--lime); display: flex; align-items: center; justify-content: space-around; font-size: 15px; font-weight: 500; color: var(--forest-deep); }
  .contact { display: flex; align-items: center; gap: 8px; }
  .contact svg { width: 18px; height: 18px; }
</style>
</head>
<body>
<main class="flyer">
  <div class="abs hero-shape"></div>
  <div class="abs hero-photo" role="img" aria-label="Photo of a smiling woman in a yellow top using her phone on a sofa"></div>
  <div class="abs brand"><span class="brand-dot"></span><span class="brand-name">Larkfield Clinic</span></div>
  <h1 class="abs headline">Helping Bodies<br>Helping Minds<br>Helping You</h1>

  <div class="abs band" style="top:222px"><h2>Mental Health Providers</h2></div>
  <p class="abs intro" style="top:270px">Bringing comprehensive evaluation, medication management and psychotherapy to the full spectrum of mental health disorders including minor, moderate and major depression, bipolar disorder, ADD/ADHD, anxiety, schizophrenia, stress or grief reactions, and others.</p>

  <div class="abs provider-panel"></div>
  <div class="abs provider-curve"></div>
  <div class="abs providers">
    <article class="provider">
      <div class="provider-photo" role="img" aria-label="Portrait photo of Owen Marlow"></div>
      <p class="provider-name">Owen Marlow,<br>PMHNP - BC</p>
      <p class="provider-bio">Before entering into healthcare, Owen spent years in academia researching foundational cellular and molecular biology mechanisms along with genetics that has provided a strong basis for understanding complex psychiatric conditions and the medications used in behavioral health. Owen cares for teenagers thru adult patient populations.</p>
    </article>
    <article class="provider">
      <div class="provider-photo" role="img" aria-label="Portrait photo of Tessa Whitcomb"></div>
      <p class="provider-name">Tessa Whitcomb,<br>PMHNP - BC</p>
      <p class="provider-bio">With a former career in the inpatient behavioral health environment, Tessa is excited to share her experience and passion for mental health in an outpatient setting. Her practice cares for teenagers to adults in all aspects of psychiatry and mental wellness.</p>
    </article>
    <article class="provider">
      <div class="provider-photo" role="img" aria-label="Portrait photo of Gil Aldridge"></div>
      <p class="provider-name">Gil Aldridge<br>PMHNP - BC</p>
      <p class="provider-bio">Formerly from the northern valley and having moved back to this area, Gil brings several years of pediatric and adolescent experience to Larkfield Clinic. Outside of work, Gil enjoys spending time with his wife and two children, exploring various outdoor pursuits including backpacking, fishing.</p>
    </article>
    <article class="provider">
      <div class="provider-photo" role="img" aria-label="Portrait photo of Maren Coldwell"></div>
      <p class="provider-name">Maren Coldwell,<br>PMHNP-BC</p>
      <p class="provider-bio">Dr. Maren Coldwell is Board Certified in Geriatric and Adult Psychiatric Medicine. She has practiced Psychiatry for over 30 years and has extensive experience in the diagnosis and treatment of major mental illnesses. Her passion for mental wellness values the long term relationship with the adult and geriatric patient.</p>
    </article>
  </div>

  <div class="abs band" style="top:708px"><h2>Migraine and Neurospasticity Intervention</h2></div>
  <div class="abs spec-circle"></div>
  <p class="abs intro" style="top:754px">Injections of botulinum neurotoxin are a widely used therapeutic form of treatment for both chronic migraines and patients with involuntary muscle contractions (neurospasticity). Injections may offer up to 3 months of relief and may be combined with other pharmaceutical interventions for maximum benefit.</p>

  <section class="abs specialist">
    <div class="specialist-photo" role="img" aria-label="Portrait photo of Dr. Dale Pennington"></div>
    <p class="specialist-bio">A board certified family practice physician, Dr. Dale Pennington has incorporated botulinum toxin injections into his practice for several years. Now retired from family medicine, he is devoted to helping patients find relief from migraines and muscle spasticity issues.</p>
  </section>

  <section class="abs steps">
    <div class="step">
      <svg viewBox="0 0 54 54" fill="none" stroke="var(--forest-deep)" stroke-width="3"><path d="M6 8h42v28H22l-10 9v-9H6z"/><circle cx="18" cy="22" r="2" fill="var(--forest-deep)"/><circle cx="27" cy="22" r="2" fill="var(--forest-deep)"/><circle cx="36" cy="22" r="2" fill="var(--forest-deep)"/></svg>
      <h3>New Patient<br>Evaluation</h3>
      <p>Consults provided for evaluation and management of patients with chronic migraines or neurospasticity challenges</p>
    </div>
    <div class="step alt">
      <svg viewBox="0 0 54 54" fill="none" stroke="var(--forest-deep)" stroke-width="3"><path d="M12 6h30v42H12z"/><path d="M8 14h8M8 24h8M8 34h8M20 16h16M20 24h16M20 32h10"/></svg>
      <h3>Insurance Pre-<br>Authorization</h3>
      <p>Botulinum toxin injections may be a recommended treatment option. If so, our office completes insurance pre-authorizations on your behalf.</p>
    </div>
    <div class="step">
      <svg viewBox="0 0 54 54" fill="none" stroke="var(--forest-deep)" stroke-width="3"><rect x="6" y="10" width="42" height="38"/><path d="M6 20h42M16 5v9M38 5v9"/><rect x="13" y="26" width="7" height="6"/><rect x="24" y="26" width="7" height="6"/><rect x="35" y="26" width="7" height="6"/><rect x="13" y="36" width="7" height="6"/><rect x="24" y="36" width="7" height="6"/><rect x="35" y="36" width="7" height="6"/></svg>
      <h3>Follow-Up<br>Appointments</h3>
      <p>Timely appointments following insurance approval are available to quickly get you on the road to relief.</p>
    </div>
  </section>

  <footer class="abs footer">
    <span class="contact"><svg viewBox="0 0 24 24" fill="var(--forest-deep)"><path d="M6.6 10.8a15 15 0 0 0 6.6 6.6l2.2-2.2a1 1 0 0 1 1-.25 11.4 11.4 0 0 0 3.6.57 1 1 0 0 1 1 1V20a1 1 0 0 1-1 1A17 17 0 0 1 3 4a1 1 0 0 1 1-1h3.5a1 1 0 0 1 1 1c0 1.25.2 2.45.57 3.6a1 1 0 0 1-.25 1z"/></svg>555-014-2290</span>
    <span class="contact"><svg viewBox="0 0 24 24" fill="var(--forest-deep)"><path d="M2 5h20v14H2zm2 2v.5l8 5 8-5V7z"/></svg>support@LarkfieldCare.example</span>
    <span class="contact"><svg viewBox="0 0 24 24" fill="none" stroke="var(--forest-deep)" stroke-width="2"><circle cx="12" cy="12" r="9"/><path d="M3 12h18M12 3c3 3 3 15 0 18M12 3c-3 3-3 15 0 18"/></svg>https://www.larkfieldcare.example/</span>
  </footer>
</main>
</body>
</html>
```